Bref créative
Stationary, Envelope, and Business Card Designs for an Accounting/Bookkeeping company
R&K Ledger and Audit Partners, LLC
Professional
Doug M. Prentt
Partner, Chief Financial Officer
41207 Route 53
Haines City, FL 33844
dprentt@rkbooksco.com
www.rkbooksco.com
R&K Ledger and Audit Partners, LLC Logo in AI format - full color.
Logo color specifics.

```html
<!DOCTYPE html>
<html lang="en">
<head>
<meta charset="utf-8">
<title>R&amp;K Ledger and Audit Partners, LLC — Business Card</title>
<link href="https://fonts.googleapis.com/css2?family=Marcellus+SC&family=Lato:wght@400;700&display=swap" rel="stylesheet">
<style>
  :root {
    --bg-top: #e2e2e2;
    --bg-bottom: #b5b5b5;
    --card: #ffffff;
    --brand-blue: #1d5fae;
    --back-light: #1f8fce;
    --back-mid: #1d62b0;
    --back-deep: #173e8c;
    --brand-green: #6cb23f;
    --text-grey: #6f6f6f;
    --rule: #e6e6e6;
    --on-blue: #ffffff;
  }
  * { margin: 0; padding: 0; box-sizing: border-box; }
  html, body { width: 1200px; height: 901px; overflow: hidden; }
  body {
    background: radial-gradient(ellipse at 50% 40%, var(--bg-top), var(--bg-bottom));
    display: flex; align-items: center; justify-content: center; gap: 36px;
    font-family: "Lato", sans-serif;
  }
  .card {
    position: relative;
    width: 560px; height: 320px;
    box-shadow: 0 14px 32px rgba(0,0,0,0.25);
    overflow: hidden;
  }

  /* Back side */
  .card-back {
    background: linear-gradient(125deg, var(--back-light) 0%, var(--back-mid) 50%, var(--back-deep) 100%);
  }
  .back-name {
    position: absolute; right: 34px; top: 150px;
    width: 300px; text-align: right;
    font-family: "Marcellus SC", serif;
    font-size: 24px; line-height: 1.15;
    color: var(--on-blue);
  }

  /* Front side */
  .card-front { background: var(--card); }
  .brand-lockup {
    position: absolute; left: 30px; top: 30px;
    display: flex; align-items: center; gap: 10px;
  }
  .brand-mark {
    width: 34px; height: 34px; border-radius: 50%;
    background: var(--brand-blue); flex: none;
  }
  .brand-name {
    font-family: "Marcellus SC", serif;
    font-size: 16px; line-height: 1.1;
    color: var(--brand-blue);
    max-width: 200px;
  }
  .contact-block { position: absolute; left: 100px; top: 112px; }
  .person-name {
    font-family: "Marcellus SC", serif;
    font-size: 20px; font-weight: 400;
    color: var(--brand-green);
  }
  .person-title {
    font-size: 9px; color: var(--text-grey);
    margin-top: 2px; padding-bottom: 6px;
    border-bottom: 1px solid var(--rule);
    width: 210px;
    font-variant: small-caps; letter-spacing: 0.5px;
  }
  .address {
    margin-top: 16px;
    font-size: 9px; line-height: 1.5; color: var(--text-grey);
  }
  .contact-list { list-style: none; margin-top: 6px; }
  .contact-list li {
    display: flex; align-items: center; gap: 6px;
    font-size: 9px; line-height: 1.6; color: var(--text-grey);
  }
  .contact-list svg { width: 8px; height: 8px; flex: none; }
</style>
</head>
<body>
  <section class="card card-back">
    <p class="back-name">R&amp;K Ledger and Audit Partners, LLC</p>
  </section>

  <section class="card card-front">
    <header class="brand-lockup">
      <span class="brand-mark"></span>
      <span class="brand-name">R&amp;K Ledger and Audit Partners, LLC</span>
    </header>

    <div class="contact-block">
      <h1 class="person-name">Doug M. Prentt</h1>
      <p class="person-title">Partner, Chief Financial Officer</p>
      <p class="address">41207 Route 53<br>Haines City, FL 33844</p>
      <ul class="contact-list">
        <li><svg viewBox="0 0 12 12"><circle cx="6" cy="6" r="5" fill="#6cb23f"/></svg>(555) 201-4400</li>
        <li><svg viewBox="0 0 12 12"><circle cx="6" cy="6" r="5" fill="#6cb23f"/></svg>(555) 201-4401</li>
        <li><svg viewBox="0 0 12 12"><circle cx="6" cy="6" r="5" fill="#6cb23f"/></svg>(555) 201-4402</li>
        <li><svg viewBox="0 0 12 12"><rect x="1" y="2.5" width="10" height="7" fill="none" stroke="#6cb23f" stroke-width="1.4"/><path d="M1 2.5 L6 7 L11 2.5" fill="none" stroke="#6cb23f" stroke-width="1.4"/></svg>dprentt@rkbooksco.com</li>
        <li><svg viewBox="0 0 12 12"><circle cx="6" cy="6" r="5" fill="none" stroke="#6cb23f" stroke-width="1.4"/><path d="M1 6 H11 M6 1 V11" stroke="#6cb23f" stroke-width="1"/></svg>www.rkbooksco.com</li>
      </ul>
    </div>
  </section>
</body>
</html>
```